Patternmaking service (fashion) card design

I need cards for my patternmaking service. I service both large and small fashion labels including ladies,mens and childrenswear. I would like cards that have a sort of vintage feel, especially 50's and 60's style. Pink is my signature colour. Its important to have a fashion reference of some kind.

Industry/Entity Type

Fashion

Contact Information for Business Card

Marigold Thimble, Patternmaking Service, Kessa Vantorin,
27 Pellham Lane. Ashbrook Vale. VIC. 3152. 0415836204, email:lacebird4@mailnest.example. "By appointment only"

```html
<!DOCTYPE html>
<html lang="en">
<head>
<meta charset="utf-8">
<title>Marigold Thimble – Patternmaking Service</title>
<link rel="stylesheet" href="https://fonts.googleapis.com/css2?family=Kaushan+Script&family=Questrial&display=swap">
<style>
  :root {
    --paper: #fdf4f7;
    --blossom: #f5bfdc;
    --blossom-deep: #e99ccb;
    --lilac: #efb4e4;
    --butter: #f9e9b8;
    --band: #f4b0d0;
    --title: #7c1f44;
    --contact: #5b1f52;
  }
  html, body {
    margin: 0;
    padding: 0;
    width: 1200px;
    height: 686px;
    overflow: hidden;
    background: var(--paper);
  }
  .card {
    position: relative;
    width: 1200px;
    height: 686px;
    overflow: hidden;
    background: var(--paper);
  }
  .floral-backdrop {
    position: absolute;
    inset: 0;
    width: 1200px;
    height: 686px;
  }
  .title-band {
    position: absolute;
    left: 0;
    top: 158px;
    width: 1200px;
    height: 50px;
    background: linear-gradient(180deg,
      rgba(244,176,208,0) 0%,
      rgba(244,176,208,0.9) 30%,
      rgba(238,150,192,0.95) 50%,
      rgba(244,176,208,0.9) 70%,
      rgba(244,176,208,0) 100%);
  }
  .service-title {
    position: absolute;
    left: 0;
    top: 118px;
    width: 1200px;
    margin: 0;
    text-align: center;
    font-family: "Kaushan Script", cursive;
    font-weight: 400;
    font-size: 80px;
    line-height: 110px;
    letter-spacing: 3px;
    color: var(--title);
    text-indent: -2px;
  }
  .service-range {
    position: absolute;
    left: 0;
    top: 226px;
    width: 1200px;
    margin: 0;
    text-align: center;
    font-family: "Kaushan Script", cursive;
    font-size: 29px;
    line-height: 40px;
    letter-spacing: 2.5px;
    color: var(--title);
    text-indent: -6px;
  }
  .contact {
    position: absolute;
    left: 90px;
    top: 512px;
    width: 1022px;
    font-family: "Questrial", sans-serif;
    font-style: italic;
    font-size: 25px;
    color: var(--contact);
    line-height: 34.5px;
  }
  .contact-line {
    display: flex;
    justify-content: space-between;
    white-space: nowrap;
  }
  .appointment {
    font-weight: 700;
    padding-right: 52px;
  }
</style>
</head>
<body>
  <main class="card">
    <svg class="floral-backdrop" role="img" aria-label="Soft pink, lilac and pale yellow vintage floral wallpaper pattern with two large mirrored blossoms in the middle and smaller flowers and leaves around the edges" viewBox="0 0 1200 686" preserveAspectRatio="none">
      <defs>
        <radialGradient id="bigBloom">
          <stop offset="0" stop-color="var(--lilac)" stop-opacity="0.85"/>
          <stop offset="0.55" stop-color="var(--blossom-deep)" stop-opacity="0.55"/>
          <stop offset="1" stop-color="var(--blossom)" stop-opacity="0"/>
        </radialGradient>
        <radialGradient id="smallBloom">
          <stop offset="0" stop-color="var(--blossom-deep)" stop-opacity="0.6"/>
          <stop offset="1" stop-color="var(--blossom)" stop-opacity="0"/>
        </radialGradient>
        <radialGradient id="leafWash">
          <stop offset="0" stop-color="var(--butter)" stop-opacity="0.95"/>
          <stop offset="1" stop-color="var(--butter)" stop-opacity="0"/>
        </radialGradient>
      </defs>
      <rect width="1200" height="686" fill="var(--paper)"/>
      <ellipse cx="600" cy="300" rx="230" ry="200" fill="url(#leafWash)"/>
      <ellipse cx="170" cy="200" rx="200" ry="160" fill="url(#leafWash)"/>
      <ellipse cx="1030" cy="200" rx="200" ry="160" fill="url(#leafWash)"/>
      <ellipse cx="300" cy="640" rx="220" ry="120" fill="url(#leafWash)"/>
      <ellipse cx="900" cy="640" rx="220" ry="120" fill="url(#leafWash)"/>
      <ellipse cx="370" cy="380" rx="260" ry="210" fill="url(#bigBloom)"/>
      <ellipse cx="830" cy="380" rx="260" ry="210" fill="url(#bigBloom)"/>
      <circle cx="255" cy="70" r="120" fill="url(#smallBloom)"/>
      <circle cx="945" cy="70" r="120" fill="url(#smallBloom)"/>
      <circle cx="60" cy="40" r="130" fill="url(#smallBloom)"/>
      <circle cx="1140" cy="40" r="130" fill="url(#smallBloom)"/>
      <circle cx="120" cy="300" r="110" fill="url(#smallBloom)"/>
      <circle cx="1080" cy="300" r="110" fill="url(#smallBloom)"/>
      <circle cx="50" cy="560" r="140" fill="url(#smallBloom)"/>
      <circle cx="1150" cy="560" r="140" fill="url(#smallBloom)"/>
      <circle cx="600" cy="60" r="110" fill="url(#smallBloom)"/>
      <circle cx="600" cy="660" r="120" fill="url(#smallBloom)"/>
    </svg>

    <div class="title-band"></div>
    <h1 class="service-title">Patternmaking Service</h1>
    <p class="service-range">Ladies,Mens and Childrenswear</p>

    <address class="contact">
      <div class="contact-line"><span>Marigold Thimble, Patternmaking Service, Kessa Vantorin, 27 Pellham Lane.</span></div>
      <div class="contact-line"><span>Ashbrook Vale. VIC. 3152.</span><span class="appointment">“By Appointment Only”</span></div>
      <div class="contact-line"><span>Telephone: (415) 836 - 204</span><span>Email:lacebird4@mailnest.example</span></div>
    </address>
  </main>
</body>
</html>
```